Recreate a graphic of The Church Year

Take the uploaded graphic and recreate it (without the shield) for use by PWD, branding it with the PDW logo.

Target Market(s)

For use by PDW

Industry/Entity Type

Education

Font styles to use
Sans Serif

Requirements
Must have
• Use liturgical colors as in upload.
• The center of the circle must be empty except for the words The Church Year
• The PDW logo must be on the graphic
Nice to have
• None.

```html
<!DOCTYPE html>
<html lang="en">
<head>
<meta charset="utf-8">
<title>The Church Year — PDW</title>
<link rel="stylesheet" href="https://fonts.googleapis.com/css2?family=Arimo:wght@400;700&display=swap">
<style>
  :root {
    --brand-blue: #1877b2;
    --advent: #2e3192;
    --christmas-orange: #f18a21;
    --epiphany-green: #1f8a3d;
    --ordinary-green: #1b7a3a;
    --deep-green: #1e3a1c;
    --lent: #5a1f5a;
    --lent-label: #3b1240;
    --passion-red: #c4202a;
    --pentecost-red: #e8232a;
    --dot-red: #b5202e;
    --ink: #111111;
    --paper: #ffffff;
  }
  html, body { margin: 0; padding: 0; overflow: hidden; background: var(--paper); }
  .church-year { display: block; width: 1200px; height: 789px; font-family: "Arimo", Arial, sans-serif; }
  .side-band { fill: var(--brand-blue); }
  .brand-plate { fill: var(--paper); }
  .brand-name { fill: var(--brand-blue); font-size: 38px; font-weight: 400; }
  .ring-seg { fill: none; stroke-width: 27; }
  .seg-advent { stroke: var(--advent); }
  .seg-white { stroke: var(--paper); }
  .seg-green { stroke: var(--deep-green); }
  .seg-lent { stroke: var(--lent); }
  .seg-passion { stroke: var(--passion-red); }
  .seg-pentecost { stroke: var(--pentecost-red); }
  .edge { fill: none; stroke-width: 1.2; }
  .edge-green { stroke: var(--epiphany-green); }
  .edge-orange { stroke: var(--christmas-orange); }
  .edge-blue { stroke: var(--brand-blue); }
  .divider { stroke: var(--paper); stroke-width: 2; }
  .divider-orange { stroke: var(--christmas-orange); stroke-width: 2; }
  .ring-text { font-size: 11px; font-weight: 700; text-anchor: middle; dominant-baseline: central; }
  .ring-text-light { fill: var(--paper); }
  .ring-text-orange { fill: var(--christmas-orange); }
  .event-dot { fill: var(--dot-red); }
  .event-label { fill: var(--ink); font-size: 9.5px; }
  .event-label-end { text-anchor: end; }
  .start-dot { fill: var(--advent); }
  .start-label { fill: var(--passion-red); font-size: 9.5px; text-anchor: middle; }
  .season-box { stroke: none; }
  .season-box-outline { fill: var(--paper); stroke: #555; stroke-width: 1; }
  .season-name { font-size: 14px; font-weight: 700; fill: var(--paper); text-anchor: middle; dominant-baseline: central; }
  .season-name-orange { fill: var(--christmas-orange); font-size: 16px; }
  .season-sub { font-size: 10px; fill: var(--paper); text-anchor: middle; }
  .title { font-size: 24px; font-weight: 700; fill: var(--ink); text-anchor: middle; }
</style>
</head>
<body>
<svg class="church-year" viewBox="0 0 850 559" xmlns="http://www.w3.org/2000/svg" role="img" aria-label="The Church Year: a ring of liturgical seasons">
  <!-- brand column -->
  <rect class="side-band" x="0" y="0" width="158" height="559"/>
  <rect class="brand-plate" x="0" y="43" width="152" height="99"/>
  <text class="brand-name" x="76" y="108" text-anchor="middle">PDW</text>

  <!-- ring segments (pathLength 360, rotated from 12 o'clock) -->
  <g class="ring">
    <circle class="ring-seg seg-advent"    cx="490" cy="285" r="181.5" pathLength="360" stroke-dasharray="38 322"  transform="rotate(243 490 285)"/>
    <circle class="ring-seg seg-white"     cx="490" cy="285" r="181.5" pathLength="360" stroke-dasharray="29 331"  transform="rotate(-79 490 285)"/>
    <circle class="ring-seg seg-green"     cx="490" cy="285" r="181.5" pathLength="360" stroke-dasharray="32 328"  transform="rotate(-50 490 285)"/>
    <circle class="ring-seg seg-lent"      cx="490" cy="285" r="181.5" pathLength="360" stroke-dasharray="78 282"  transform="rotate(-18 490 285)"/>
    <circle class="ring-seg seg-passion"   cx="490" cy="285" r="181.5" pathLength="360" stroke-dasharray="10 350"  transform="rotate(60 490 285)"/>
    <circle class="ring-seg seg-white"     cx="490" cy="285" r="181.5" pathLength="360" stroke-dasharray="56 304"  transform="rotate(70 490 285)"/>
    <circle class="ring-seg seg-pentecost" cx="490" cy="285" r="181.5" pathLength="360" stroke-dasharray="5 355"   transform="rotate(126 490 285)"/>
    <circle class="ring-seg seg-green"     cx="490" cy="285" r="181.5" pathLength="360" stroke-dasharray="3 357"   transform="rotate(134 490 285)"/>
    <circle class="ring-seg seg-green"     cx="490" cy="285" r="181.5" pathLength="360" stroke-dasharray="94 266"  transform="rotate(138 490 285)"/>
    <circle class="ring-seg seg-green"     cx="490" cy="285" r="181.5" pathLength="360" stroke-dasharray="10 350"  transform="rotate(233 490 285)"/>

    <!-- outlines -->
    <circle class="edge edge-green"  cx="490" cy="285" r="195" pathLength="360" stroke-dasharray="112 248" transform="rotate(126 490 285)"/>
    <circle class="edge edge-green"  cx="490" cy="285" r="168" pathLength="360" stroke-dasharray="112 248" transform="rotate(126 490 285)"/>
    <circle class="edge edge-blue"   cx="490" cy="285" r="195" pathLength="360" stroke-dasharray="38 322"  transform="rotate(243 490 285)"/>
    <circle class="edge edge-orange" cx="490" cy="285" r="195" pathLength="360" stroke-dasharray="29 331"  transform="rotate(-79 490 285)"/>
    <circle class="edge edge-orange" cx="490" cy="285" r="168" pathLength="360" stroke-dasharray="29 331"  transform="rotate(-79 490 285)"/>
    <circle class="edge edge-green"  cx="490" cy="285" r="195" pathLength="360" stroke-dasharray="32 328"  transform="rotate(-50 490 285)"/>
    <circle class="edge edge-green"  cx="490" cy="285" r="168" pathLength="360" stroke-dasharray="32 328"  transform="rotate(-50 490 285)"/>
    <circle class="edge edge-blue"   cx="490" cy="285" r="195" pathLength="360" stroke-dasharray="88 272"  transform="rotate(-18 490 285)"/>
    <circle class="edge edge-orange" cx="490" cy="285" r="195" pathLength="360" stroke-dasharray="56 304"  transform="rotate(70 490 285)"/>
    <circle class="edge edge-orange" cx="490" cy="285" r="168" pathLength="360" stroke-dasharray="56 304"  transform="rotate(70 490 285)"/>

    <!-- dividers -->
    <line class="divider-orange" x1="490" y1="90" x2="490" y2="117" transform="rotate(40 490 285)"/>
    <line class="divider" x1="490" y1="90" x2="490" y2="117" transform="rotate(72 490 285)"/>
    <line class="divider-orange" x1="490" y1="90" x2="490" y2="117" transform="rotate(160 490 285)"/>
    <line class="divider" x1="490" y1="90" x2="490" y2="117" transform="rotate(227.5 490 285)"/>
    <line class="divider" x1="490" y1="90" x2="490" y2="117" transform="rotate(323 490 285)"/>
    <line class="divider" x1="490" y1="90" x2="490" y2="117" transform="rotate(333 490 285)"/>

    <!-- ring captions -->
    <text class="ring-text ring-text-light"  transform="translate(465 106) rotate(-8)">4 Sundays</text>
    <text class="ring-text ring-text-orange" transform="translate(566 121) rotate(25)">12 Days</text>
    <text class="ring-text ring-text-orange" transform="translate(640 184) rotate(56)">4-8 Sundays</text>
    <text class="ring-text ring-text-orange" transform="translate(668 316) rotate(100)">5 Sundays</text>
    <text class="ring-text ring-text-orange" transform="translate(601 428) rotate(142)">7 Days</text>
    <text class="ring-text ring-text-orange" transform="translate(465 464) rotate(188)">50 Days</text>
  </g>

  <text class="title" x="490" y="295">The Church Year</text>

  <!-- start marker -->
  <circle class="start-dot" cx="424" cy="160" r="3"/>
  <text class="start-label" x="458" y="163">The Church Year</text>
  <text class="start-label" x="458" y="174">Begins Here</text>

  <!-- feast days -->
  <g class="events">
    <circle class="event-dot" cx="531" cy="87" r="3"/><text class="event-label" x="537" y="91">Birth of Our Lord (Christmas Eve, Christmas Day)</text>
    <circle class="event-dot" cx="612" cy="125" r="3"/><text class="event-label" x="619" y="129">Day of Epiphany</text>
    <circle class="event-dot" cx="621" cy="137" r="3"/><text class="event-label" x="627" y="141">Baptism of Our Lord</text>
    <circle class="event-dot" cx="678" cy="210" r="3"/><text class="event-label" x="684" y="214">Transfiguration</text>
    <circle class="event-dot" cx="684" cy="223" r="3"/><text class="event-label" x="690" y="227">Ash Wednesday</text>
    <circle class="event-dot" cx="642" cy="421" r="3"/><text class="event-label" x="649" y="425">Passion (Palm) Sunday</text>
    <circle class="event-dot" cx="615" cy="444" r="3"/><text class="event-label" x="622" y="448">Maundy Thursday</text>
    <circle class="event-dot" cx="592" cy="457" r="3"/><text class="event-label" x="599" y="461">The Passion of Our Lord (Good Friday)</text>
    <circle class="event-dot" cx="570" cy="469" r="3"/><text class="event-label" x="577" y="473">The Resurrection of Our Lord (Easter Sunday)</text>
    <circle class="event-dot" cx="428" cy="477" r="3"/><text class="event-label event-label-end" x="422" y="481">The Ascension of Our Lord</text>
    <circle class="event-dot" cx="363" cy="441" r="3"/><text class="event-label event-label-end" x="357" y="445">Day of Pentecost</text>
    <circle class="event-dot" cx="351" cy="431" r="3"/><text class="event-label event-label-end" x="345" y="435">Holy Trinity Sunday</text>
    <circle class="event-dot" cx="366" cy="124" r="3"/><text class="event-label event-label-end" x="360" y="128">All Saints Day</text>
    <circle class="event-dot" cx="396" cy="104" r="3"/><text class="event-label event-label-end" x="390" y="108">Christ the King Sunday</text>
  </g>

  <!-- season labels -->
  <g class="seasons">
    <rect class="season-box" x="330" y="55" width="122" height="21" fill="var(--advent)"/>
    <text class="season-name" x="391" y="65.5">Advent Season</text>

    <rect class="season-box-outline" x="565" y="37" width="170" height="29" rx="3"/>
    <text class="season-name season-name-orange" x="650" y="51.5">Christmas Season</text>

    <rect class="season-box" x="678" y="164" width="144" height="20" fill="var(--epiphany-green)"/>
    <text class="season-name" x="750" y="174">Epiphany Season</text>

    <rect class="season-box" x="701" y="308" width="121" height="23" fill="var(--lent-label)"/>
    <text class="season-name" x="761.5" y="319.5">Season of Lent</text>

    <rect class="season-box" x="637" y="492" width="88" height="21" fill="var(--passion-red)"/>
    <text class="season-name" x="681" y="502.5">Holy Week</text>

    <rect class="season-box-outline" x="340" y="502" width="138" height="27" rx="3"/>
    <text class="season-name season-name-orange" x="409" y="515.5">Easter Season</text>

    <rect class="season-box" x="184" y="190" width="139" height="39" rx="2" fill="var(--ordinary-green)"/>
    <text class="season-name" x="253.5" y="204">Ordinary Time</text>
    <text class="season-sub" x="253.5" y="222">(Time after Pentecost)</text>
  </g>
</svg>
</body>
</html>
```